K & D A/C Compressors' Business Card

Hello,

I need someone to create a new business card for my business. The name of my Business is: K & D A/C Compressors. I sell automotive air conditioning parts (a/c parts). I would like the business card to incorporate my logo, and to have an automotive feel to it. It is important that the business card feel like it is coming from an automotive parts business.

I already have a logo, which I will provide.

Thanks.
Updates

Project Deadline Extended Reason: I feel like extending the deadline until October 9, 2017, will allow for more time to design the business card. Thank you for your understanding. Added Monday, October 2, 2017

Target Market(s)

Consumers who need automotive a/c parts, and auto mechanics.

Industry/Entity Type

Automotive

Contact Information for Business Card

Business name: K & D A/C Compressors
Business Address: 48207 Southwest 36th Street, Palm Crest, Florida 33990
Telephone: 305-472-1390
Fax: To be provided once I choose your design.
Website: www.kdcoolunits.example
Email: support@kdcoolunits.example
Names: To be provided once I choose your design.

Font styles to use
Sans Serif

Colors

Designer to choose colors to be used in the design.

Requirements
Must have
• The business card must include all of the "Business Card Details" and the logo I have uploaded.

```html
<!DOCTYPE html>
<html lang="en">
<head>
<meta charset="utf-8">
<title>K &amp; D A/C Compressors – Business Card</title>
<link href="https://fonts.googleapis.com/css2?family=EB+Garamond:wght@400;500&display=swap" rel="stylesheet">
<style>
  :root {
    --page-bg: #c9ced6;
    --card-bg: #1f2022;
    --accent-blue: #2a9fd8;
    --text-light: #c9ccd1;
    --text-muted: #8e9297;
    --photo-dark: #2b3038;
    --photo-mid: #6d7784;
    --photo-light: #c3cbd4;
  }
  * { box-sizing: border-box; margin: 0; padding: 0; }
  html, body { width: 1200px; height: 1000px; overflow: hidden; }
  body {
    background: linear-gradient(180deg, #e4e7ec 0%, var(--page-bg) 100%);
    font-family: "EB Garamond", Georgia, serif;
    position: relative;
  }
  .card {
    position: absolute;
    width: 500px;
    height: 286px;
    background: var(--card-bg);
    overflow: hidden;
    box-shadow: 0 18px 40px rgba(40, 50, 65, 0.25);
  }
  .card-edge {
    position: absolute;
    top: 0; bottom: 0;
    width: 7px;
    background: var(--accent-blue);
  }
  /* Front side */
  .card-front { left: 70px; top: 580px; }
  .card-front .card-edge { left: 0; }
  .contact-panel {
    position: absolute;
    left: 30px; top: 38px;
    width: 194px;
  }
  .holder-name {
    color: var(--accent-blue);
    font-size: 19px;
    font-weight: 400;
    letter-spacing: 0.5px;
    text-transform: uppercase;
    line-height: 1.1;
    white-space: nowrap;
  }
  .holder-title {
    color: var(--text-light);
    font-size: 13px;
    margin-top: 4px;
  }
  .address {
    color: var(--text-light);
    font-size: 10.5px;
    line-height: 1.35;
    margin-top: 22px;
  }
  .contact-list { list-style: none; margin-top: 14px; }
  .contact-item {
    display: flex;
    align-items: center;
    gap: 9px;
    color: var(--text-light);
    font-size: 10.5px;
    letter-spacing: 0.6px;
    height: 21px;
    white-space: nowrap;
  }
  .contact-icon { width: 14px; height: 14px; flex: none; }
  .interior-photo {
    position: absolute;
    left: 228px; top: 0;
    width: 272px; height: 286px;
    background:
      radial-gradient(ellipse at 35% 55%, var(--photo-dark) 0%, transparent 55%),
      linear-gradient(135deg, var(--photo-light) 0%, var(--photo-mid) 45%, var(--photo-dark) 100%);
  }
  /* Back side */
  .card-back { left: 630px; top: 140px; }
  .card-back .card-edge { right: 0; }
  .brand-name {
    position: absolute;
    left: 0; right: 0; top: 128px;
    display: flex;
    align-items: center;
    justify-content: center;
    gap: 10px;
    color: var(--text-muted);
    font-size: 22px;
    font-weight: 500;
    letter-spacing: 0.5px;
  }
  .brand-mark { width: 14px; height: 14px; background: var(--accent-blue); }
</style>
</head>
<body>

<section class="card card-back" aria-label="Business card back">
  <div class="brand-name"><span class="brand-mark"></span>K &amp; D A/C Compressors</div>
  <div class="card-edge"></div>
</section>

<section class="card card-front" aria-label="Business card front">
  <div class="card-edge"></div>
  <div class="contact-panel">
    <h1 class="holder-name">Marc Del Ruiz</h1>
    <p class="holder-title">General Manager</p>
    <p class="address">48207 Southwest 36th Street,<br>Palm Crest, Florida 33990</p>
    <ul class="contact-list">
      <li class="contact-item">
        <svg class="contact-icon" viewBox="0 0 14 14"><circle cx="7" cy="7" r="7" fill="#2a9fd8"/><path d="M4.3 3.8c.4-.4.9-.4 1.1 0l.6 1.1c.2.3.1.6-.2.8l-.4.3c.4.9 1 1.5 1.9 1.9l.3-.4c.2-.3.5-.4.8-.2l1.1.6c.4.2.4.7 0 1.1l-.5.5c-.5.5-1.3.5-2-.1-1.3-.8-2.4-1.9-3.2-3.2-.5-.7-.5-1.5 0-2z" fill="#fff"/></svg>
        305-472-1390
      </li>
      <li class="contact-item">
        <svg class="contact-icon" viewBox="0 0 14 14"><circle cx="7" cy="7" r="7" fill="#2a9fd8"/><rect x="4" y="6" width="6" height="3.5" fill="#fff"/><rect x="5" y="3.5" width="4" height="2.2" fill="#fff"/><rect x="5" y="8.5" width="4" height="2" fill="#2a9fd8" stroke="#fff" stroke-width=".6"/></svg>
        305 610 2754
      </li>
      <li class="contact-item">
        <svg class="contact-icon" viewBox="0 0 14 14"><circle cx="7" cy="7" r="7" fill="#2a9fd8"/><rect x="3.5" y="4.5" width="7" height="5" fill="none" stroke="#fff" stroke-width=".9"/><path d="M3.5 4.5 7 7.3l3.5-2.8" fill="none" stroke="#fff" stroke-width=".9"/></svg>
        support@kdcoolunits.example
      </li>
      <li class="contact-item">
        <svg class="contact-icon" viewBox="0 0 14 14"><circle cx="7" cy="7" r="7" fill="#2a9fd8"/><circle cx="7" cy="7" r="3.6" fill="none" stroke="#fff" stroke-width=".8"/><ellipse cx="7" cy="7" rx="1.5" ry="3.6" fill="none" stroke="#fff" stroke-width=".8"/><path d="M3.4 7h7.2" stroke="#fff" stroke-width=".8"/></svg>
        www.kdcoolunits.example
      </li>
    </ul>
  </div>
  <div class="interior-photo" role="img" aria-label="Photo of a car interior with steering wheel and dashboard"></div>
</section>

</body>
</html>
```